Fernbrook Pet Showcase Ticket Card Design

We’re looking to create a complimentary “ticket” card for Fernbrook Pet Showcase that can be handed out physically. We host an event for cat lovers. The card should feel special and collectible. Size will be a standard business card (3.5" x 2") Orientation is open to designer recommendation. This ticket will be used as a complimentary entry pass for select guests, partners, & giveaways. Key elements to Include are the Fernbrook Pet Showcase logo (provided), the words “Complimentary Ticket” or similar wording (open to creative phrasing and cat puns) A blank space for the Event date (to be written in) & Ticket number (to be written in) . Event Name is always "Fernbrook Pet Bazaar & Rehoming Day". We want the ticket to feel clean & modern but slightly playful with a cat-inspired touch (think clever, not kitschy). Could include a subtle cat motif or texture (e.g., whisker lines, paw detail, soft patterning) Open to unique layout ideas that still leave clear writing space. Avoid overcrowding of elements. Ticket should also have fine print "This ticket is not redeemable for cash and cannot be combined with any other offers or discounts, can only be used for the date indicated"

Target Market(s)

Women

Industry/Entity Type

pets

Colors
6B429C
8869AF
B7A5CE
E3DAEB
F3F0F8

Requirements
Must have
• Fernbrook Pet Showcase Logo & words around complimentary ticket as well as the fine print
Nice to have
• cat-inspired touch (think clever, not kitschy). Could include a subtle cat motif or texture (e.g., whisker lines, paw detail, soft patterning)
Should not have
• should not look cartoony

```html
<!DOCTYPE html>
<html lang="en">
<head>
<meta charset="utf-8">
<title>Fernbrook Pet Showcase – Complimentary Ticket</title>
<link href="https://fonts.googleapis.com/css2?family=Source+Serif+4:ital,opsz,wght@0,8..60,400;0,8..60,500;0,8..60,700;1,8..60,500&display=swap" rel="stylesheet">
<style>
  :root{
    --plum:#4f3470;
    --violet-deep:#8869AF;
    --violet:#9a85c7;
    --lilac:#B7A5CE;
    --mist:#E3DAEB;
    --paper:#F3F0F8;
    --page:#fdfdfd;
    --white:#ffffff;
  }
  *{box-sizing:border-box;margin:0;padding:0}
  html,body{width:1200px;height:1200px;overflow:hidden;background:var(--page)}
  body{position:relative;font-family:"Source Serif 4",Georgia,serif;color:var(--plum)}

  .ticket{position:absolute;left:200px;top:366px;width:806px;height:475px;background:var(--paper);overflow:hidden}

  .brand-panel{position:absolute;left:0;top:0;width:292px;height:334px;background:var(--lilac)}
  .brand-panel__pattern{position:absolute;inset:0;background:linear-gradient(180deg,#c2b2da,#b3a0cf)}
  .brand-panel__banner{position:absolute;left:0;top:0;width:292px;height:262px}
  .brand-name{position:absolute;left:0;top:112px;width:292px;text-align:center;color:var(--white);
    font-weight:700;font-size:36px;line-height:1.15}

  .top-band{position:absolute;left:292px;top:0;width:514px;height:63px;background:linear-gradient(90deg,#c0b0d9,#bba9d6)}

  .headline{position:absolute;left:323px;top:88px;width:470px}
  .headline__event{font-weight:500;font-size:31px;line-height:46px;letter-spacing:-0.2px}
  .headline__pun{font-style:italic;font-weight:500;font-size:40px;margin-top:10px;line-height:46px}
  .headline__title{font-weight:700;font-size:43px;margin-top:12px;line-height:50px;letter-spacing:-0.3px}

  .writein{position:absolute;left:0;top:334px;width:806px;height:73px;background:var(--mist)}
  .field{position:absolute;top:28px;font-size:22px;display:flex;align-items:flex-end}
  .field__line{display:inline-block;border-bottom:1.5px solid var(--plum);margin-left:6px;height:18px}
  .field--date{left:84px}
  .field--date .field__line{width:164px}
  .field--number{left:398px}
  .field--number .field__line{width:212px}

  .fine-print{position:absolute;left:0;top:407px;width:806px;height:58px;background:var(--violet);
    color:var(--white);font-size:14px;line-height:17px;text-align:center;padding:10px 26px 0 26px}
  .bottom-edge{position:absolute;left:0;top:465px;width:806px;height:10px;background:var(--lilac)}
</style>
</head>
<body>
  <section class="ticket">
    <div class="brand-panel">
      <div class="brand-panel__pattern" role="img" aria-label="Soft paw print pattern"></div>
      <svg class="brand-panel__banner" viewBox="0 0 292 262" aria-hidden="true">
        <polygon points="0,0 292,0 292,222 147,262 0,222" fill="#8869AF"/>
      </svg>
      <p class="brand-name">Fernbrook<br>Pet Showcase</p>
    </div>

    <div class="top-band" role="img" aria-label="Soft paw print pattern"></div>

    <div class="headline">
      <p class="headline__event">Fernbrook Pet Bazaar<br>&amp; Rehoming Day</p>
      <p class="headline__pun">purr-fectly</p>
      <p class="headline__title">Complimentary Ticket</p>
    </div>

    <div class="writein">
      <p class="field field--date">Event Date:<span class="field__line"></span></p>
      <p class="field field--number">Ticket No.:<span class="field__line"></span></p>
    </div>

    <p class="fine-print">This ticket is not redeemable for cash and cannot be combined with any other offers or discounts, can only be used for the date indicated.</p>
    <div class="bottom-edge"></div>
  </section>
</body>
</html>
```